Mixed Martial Arts gym that is known for high quality athletes, students and training

We need a business card designed that is unique and stands out. Something that is not so dark and boring but looks 'energetic' to those that are given it. The customers that would receive this card would be looking to sign up for martial arts or fitness training and this card is used for corporate sponsorships and networking as well.

Marcus Pellow-Grant
0417305962 or 0409561738
Level 1, 284 Wendover Road. Marlowe Vale NSW 2175
marcus@kinetiqcombatworks.com.au
www.kinetiqcombatworks.com

```html
<!DOCTYPE html>
<html lang="en">
<head>
<meta charset="utf-8">
<title>Kinetiq Combat Works – Business Card</title>
<link rel="stylesheet" href="https://fonts.googleapis.com/css2?family=Source+Sans+3:wght@400;600;700;800&display=swap">
<style>
  :root {
    --orange: #f7941d;
    --black: #0a0a0a;
    --white: #ffffff;
    --ink: #2b2b2b;
    --backdrop: #e9e6e2;
    --card-radius: 40px;
  }
  html, body {
    margin: 0;
    padding: 0;
    width: 1200px;
    height: 1089px;
    overflow: hidden;
    background: var(--backdrop);
    font-family: "Source Sans 3", Arial, sans-serif;
  }
  .canvas {
    position: relative;
    width: 1200px;
    height: 1089px;
  }
  .card {
    position: absolute;
    width: 868px;
    height: 494px;
    border-radius: var(--card-radius);
    overflow: hidden;
    box-shadow: 0 2px 6px rgba(0,0,0,0.18);
  }
  .card--front {
    left: 19px;
    top: 38px;
    background: var(--white);
  }
  .card--back {
    left: 300px;
    top: 566px;
    background: var(--black);
  }
  .card__band {
    position: absolute;
    left: 0;
    top: 0;
    width: 868px;
    height: 494px;
  }
  .brand {
    position: absolute;
    left: 0;
    right: 0;
    text-align: center;
    color: var(--orange);
    font-weight: 800;
    text-transform: uppercase;
    line-height: 0.95;
    margin: 0;
  }
  .card--front .brand {
    top: 70px;
    left: 110px;
    right: 214px;
    font-size: 80px;
    letter-spacing: 1px;
  }
  .card--back .brand {
    top: 140px;
    font-size: 96px;
    letter-spacing: 1px;
  }
  .brand__line { display: block; }
  .brand__line--small {
    font-size: 0.4em;
    letter-spacing: 7px;
    margin-top: 10px;
  }
  .holder-name {
    position: absolute;
    top: 266px;
    left: 110px;
    right: 214px;
    margin: 0;
    text-align: center;
    color: var(--orange);
    font-size: 28px;
    font-weight: 700;
  }
  .contact {
    position: absolute;
    left: 0;
    right: 0;
    margin: 0;
    text-align: center;
    color: var(--ink);
    font-size: 20px;
    font-weight: 400;
    white-space: nowrap;
  }
  .contact--phones { top: 368px; left: 40px; }
  .contact--online { top: 410px; }
  .contact--address { top: 454px; }
  .contact__item {
    display: inline-flex;
    align-items: center;
    gap: 5px;
    margin: 0 4px;
  }
  .icon {
    width: 17px;
    height: 17px;
    fill: var(--ink);
  }
  .web-address {
    position: absolute;
    left: 0;
    right: 0;
    top: 425px;
    margin: 0;
    text-align: center;
    color: var(--orange);
    font-size: 28px;
    font-weight: 400;
    letter-spacing: 3px;
  }
</style>
</head>
<body>
<main class="canvas">

  <section class="card card--front" aria-label="Business card front">
    <svg class="card__band" viewBox="0 0 868 494" aria-hidden="true">
      <path d="M0 410 Q434 234 868 410 L868 494 L0 494 Z" fill="var(--black)"/>
      <path d="M0 418 Q434 252 868 418 L868 494 L0 494 Z" fill="var(--orange)"/>
    </svg>

    <h1 class="brand">
      <span class="brand__line">Kinetiq</span>
      <span class="brand__line brand__line--small">Combat Works</span>
    </h1>

    <p class="holder-name">Marcus Pellow-Grant</p>

    <p class="contact contact--phones">
      <span class="contact__item">
        <svg class="icon" viewBox="0 0 24 24" aria-hidden="true"><path d="M6.6 10.8c1.4 2.8 3.8 5.1 6.6 6.6l2.2-2.2c.3-.3.7-.4 1-.2 1.1.4 2.3.6 3.6.6.6 0 1 .4 1 1V20c0 .6-.4 1-1 1C10.6 21 3 13.4 3 4c0-.6.4-1 1-1h3.5c.6 0 1 .4 1 1 0 1.3.2 2.5.6 3.6.1.3 0 .7-.2 1L6.6 10.8z"/></svg>
        0417305962
      </span>
      <span class="contact__item">
        <svg class="icon" viewBox="0 0 24 24" aria-hidden="true"><path d="M6.6 10.8c1.4 2.8 3.8 5.1 6.6 6.6l2.2-2.2c.3-.3.7-.4 1-.2 1.1.4 2.3.6 3.6.6.6 0 1 .4 1 1V20c0 .6-.4 1-1 1C10.6 21 3 13.4 3 4c0-.6.4-1 1-1h3.5c.6 0 1 .4 1 1 0 1.3.2 2.5.6 3.6.1.3 0 .7-.2 1L6.6 10.8z"/></svg>
        0409561738
      </span>
    </p>

    <p class="contact contact--online">
      <span class="contact__item">
        <svg class="icon" viewBox="0 0 24 24" aria-hidden="true"><path d="M2 9l10-6 10 6v11H2z M4 10v8h16v-8l-8 5z"/></svg>
        marcus@kinetiqcombatworks.com.au
      </span>
      <span class="contact__item">
        <svg class="icon" viewBox="0 0 24 24" aria-hidden="true"><path d="M12 2a10 10 0 1 0 0 20 10 10 0 0 0 0-20zm6.9 9h-3a15 15 0 0 0-1.3-5.6A8 8 0 0 1 18.9 11zM12 4.1c.9 1.3 1.7 3.8 1.9 6.9h-3.8c.2-3.1 1-5.6 1.9-6.9zM9.4 5.4A15 15 0 0 0 8.1 11h-3a8 8 0 0 1 4.3-5.6zM5.1 13h3a15 15 0 0 0 1.3 5.6A8 8 0 0 1 5.1 13zm6.9 6.9c-.9-1.3-1.7-3.8-1.9-6.9h3.8c-.2 3.1-1 5.6-1.9 6.9zm2.6-1.3a15 15 0 0 0 1.3-5.6h3a8 8 0 0 1-4.3 5.6z"/></svg>
        www.kinetiqcombatworks.com
      </span>
    </p>

    <p class="contact contact--address">Level 1, 284 Wendover Road. Marlowe Vale NSW 2175</p>
  </section>

  <section class="card card--back" aria-label="Business card back">
    <h2 class="brand">
      <span class="brand__line">Kinetiq</span>
      <span class="brand__line brand__line--small">Combat Works</span>
    </h2>
    <p class="web-address">www.kinetiqcombatworks.com</p>
  </section>

</main>
</body>
</html>
```